Simple Banners for several sites

I'm looking for banners in the following formats for the sites listed bellow:

* Leaderboard
* Wide Skyscraper
* Skyscaper
* Square Button
* Micro bar
* Full banner
* Half Banner
* Medium Rectangle

The websites:
* http://factheap.vornel.com/
* http://pagtrove.com/
* http://netolumba.com/

I would like to get 1 sets of banners for each website, and I'ld like you to submit each set/site independently.

```html
<!DOCTYPE html>
<html lang="pt">
<head>
<meta charset="utf-8">
<title>Netolumba – banners</title>
<link rel="stylesheet" href="https://fonts.googleapis.com/css2?family=Oswald:wght@300;400&family=Roboto+Condensed:wght@400;700&family=Roboto:wght@500&display=swap">
<style>
  :root {
    --stage: #1b1b1b;
    --teal-top: #6f9fb1;
    --teal-mid: #4e7f93;
    --teal-deep: #3a6577;
    --bar: #0c0c0c;
    --brand-blue: #6e97a9;
    --white: #ffffff;
    --red-top: #c5202c;
    --red-bottom: #84070f;
    --device-dark: #1e2326;
    --device-light: #d9dde0;
  }
  html, body {
    margin: 0;
    width: 1200px;
    height: 1123px;
    overflow: hidden;
    background: var(--stage);
  }
  .canvas { position: relative; width: 1200px; height: 1123px; }

  .banner {
    position: absolute;
    overflow: hidden;
    background: var(--bar);
    box-shadow: 0 4px 18px rgba(0,0,0,.6);
  }
  .banner__panel {
    position: absolute;
    left: 0; top: 0; width: 100%;
    background: linear-gradient(180deg, var(--teal-top) 0%, var(--teal-mid) 45%, var(--teal-deep) 100%);
  }
  .headline, .tagline, .slogan, .brand-name {
    position: absolute;
    left: 0; width: 100%;
    margin: 0;
    text-align: center;
    color: var(--white);
    text-shadow: 0 2px 3px rgba(0,0,0,.45);
  }
  .devices {
    position: absolute;
    background:
      radial-gradient(ellipse at 50% 40%, var(--device-light) 0 30%, transparent 31%),
      linear-gradient(180deg, #2a3033 0%, var(--device-dark) 100%);
    border-radius: 6px;
  }
  .cta {
    position: absolute;
    display: flex;
    align-items: center;
    justify-content: center;
    border-radius: 5px;
    border: 1px solid #e0545b;
    background: linear-gradient(180deg, var(--red-top) 0%, var(--red-bottom) 100%);
    color: var(--white);
    font-family: "Roboto", sans-serif;
    font-weight: 500;
    text-decoration: none;
    text-shadow: 0 1px 2px rgba(0,0,0,.5);
    box-shadow: 0 2px 6px rgba(0,0,0,.6);
  }

  /* Medium rectangle */
  .banner--rectangle { left: 109px; top: 334px; width: 547px; height: 456px; }
  .banner--rectangle .banner__panel { height: 380px; }
  .banner--rectangle .headline {
    top: 10px;
    font-family: "Roboto Condensed", sans-serif;
    font-weight: 700;
    font-size: 56px;
    line-height: 1.1;
    color: #f1f4f5;
  }
  .banner--rectangle .tagline {
    top: 78px;
    font-family: "Roboto Condensed", sans-serif;
    font-weight: 400;
    font-size: 32px;
    line-height: 1;
  }
  .banner--rectangle .devices { left: 44px; top: 148px; width: 442px; height: 226px; }
  .banner--rectangle .brand-name {
    left: 36px; top: 392px; width: auto;
    text-align: left;
    font-family: "Roboto Condensed", sans-serif;
    font-weight: 700;
    font-size: 46px;
    color: var(--brand-blue);
    text-shadow: none;
  }
  .banner--rectangle .cta { left: 301px; top: 389px; width: 209px; height: 55px; font-size: 26px; }

  /* Wide skyscraper */
  .banner--skyscraper { left: 751px; top: 77px; width: 257px; height: 968px; }
  .banner--skyscraper .banner__panel { height: 804px; }
  .banner--skyscraper .headline {
    top: 60px;
    font-family: "Oswald", sans-serif;
    font-weight: 400;
    font-size: 40px;
    line-height: 1;
  }
  .banner--skyscraper .tagline {
    top: 138px;
    font-family: "Oswald", sans-serif;
    font-weight: 300;
    font-size: 34px;
    line-height: 1.12;
  }
  .banner--skyscraper .devices { left: 0; top: 341px; width: 257px; height: 290px; border-radius: 0; }
  .banner--skyscraper .slogan {
    top: 655px;
    font-family: "Oswald", sans-serif;
    font-weight: 300;
    font-style: italic;
    font-size: 31px;
    line-height: 1.32;
  }
  .banner--skyscraper .cta { left: 27px; top: 857px; width: 209px; height: 53px; font-size: 25px; }
</style>
</head>
<body>
<main class="canvas">

  <section class="banner banner--rectangle" aria-label="Banner retângulo médio">
    <div class="banner__panel"></div>
    <h2 class="headline">NETOLUMBA –</h2>
    <p class="tagline">Desenvolvimento Web: idéias,<br>tecnologias e tutoriais</p>
    <div class="devices" role="img" aria-label="Monitor, portátil, tablet e telemóvel mostrando o blog"></div>
    <p class="brand-name">Netolumba</p>
    <a class="cta" href="http://netolumba.com/">LEARN MORE</a>
  </section>

  <section class="banner banner--skyscraper" aria-label="Banner arranha-céu largo">
    <div class="banner__panel"></div>
    <h2 class="headline">NETOLUMBA -</h2>
    <p class="tagline">Desenvolvimento<br>Web: idéias,<br>tecnologias<br>e tutoriais</p>
    <div class="devices" role="img" aria-label="Monitor e tablet mostrando o blog"></div>
    <p class="slogan">Desenvolvimento<br>Web nem sempre<br>simplificado</p>
    <a class="cta" href="http://netolumba.com/">LEARN MORE</a>
  </section>

</main>
</body>
</html>
```